Website Design mainly for sliders and icons

Two pages need to be designe, I've finished the templates, all detail requirement please check inattachment:

Mainly design: some pictures/icons and frames

```html
<!DOCTYPE html>
<html lang="en">
<head>
<meta charset="utf-8">
<title>Marrowvane – Cloud Solutions</title>
<link rel="stylesheet" href="https://fonts.googleapis.com/css2?family=Ubuntu:wght@400;500;700&family=PT+Serif&family=Arimo:wght@400;700&family=Questrial&display=swap">
<style>
:root{
  --bar:#6b6b6b;
  --sky:#5ba7ef;
  --sky-dark:#3f8fdc;
  --ink:#1f1f1f;
  --body:#555;
  --card:#e9e9e9;
  --link:#2a9bd6;
  --red:#d8222a;
  --social:#555;
  --white:#fff;
}
*{margin:0;padding:0;box-sizing:border-box}
html,body{width:1200px;height:2365px;overflow:hidden;background:var(--white)}
.page{position:relative;width:1200px;height:2365px;font-family:"Arimo",sans-serif;color:var(--ink)}
.abs{position:absolute}

.topnav{left:0;top:0;width:1200px;height:47px;background:var(--bar)}
.topnav a{position:absolute;top:12px;color:var(--white);font-family:"Ubuntu",sans-serif;font-size:19px;text-decoration:none}

.brand{left:104px;top:98px;font-family:"Ubuntu",sans-serif;font-weight:700;font-size:40px;color:#222;letter-spacing:.5px}
.contact{top:114px;font-family:"Ubuntu",sans-serif;font-weight:500;font-size:18px;color:#111;display:flex;align-items:center;gap:8px}

.banner{left:103px;top:189px;width:1017px;height:266px;border:1.5px solid #444}
.slide{position:absolute}

.ask{width:302px;height:111px;background:var(--sky);color:var(--white);font-family:"PT Serif",serif;font-size:19px;line-height:23px;padding:30px 14px 0;box-shadow:1px 1px 2px rgba(0,0,0,.35)}
.qmark{font-family:"PT Serif",serif;line-height:1}
.qmark.blue{color:var(--sky)}
.qmark.red{color:var(--red)}
.portrait{left:501px;top:607px;width:235px;height:221px;background:linear-gradient(180deg,#d9d9dc 0%,#e8b98e 45%,#9aa7c4 100%)}

.cta{left:289px;top:880px;width:637px;height:76px;background:var(--sky);color:var(--white);font-family:"PT Serif",serif;font-size:27px;display:flex;align-items:center;justify-content:center;box-shadow:2px 2px 3px rgba(0,0,0,.45)}

.intro-title{left:0;top:1008px;width:1200px;text-align:center;font-family:"PT Serif",serif;font-weight:400;font-size:27px;color:#111}
.intro-text{left:99px;top:1050px;width:1032px;font-size:18.5px;line-height:23.5px;color:var(--body)}

.service-head{top:1173px;width:303px;height:107px;background:var(--sky);color:var(--white);font-family:"PT Serif",serif;font-size:25px;display:flex;align-items:center;justify-content:center;box-shadow:2px 2px 2px rgba(0,0,0,.3)}
.service-tip{top:1279px;width:0;height:0;border-left:30px solid transparent;border-right:30px solid transparent;border-top:49px solid var(--sky)}
.service-body{top:1358px;width:303px;height:348px;background:var(--card);box-shadow:2px 2px 3px rgba(0,0,0,.4);padding:34px 20px 0 27px;font-family:"PT Serif",serif;font-size:17.5px;line-height:23px;color:#222}

.section-title{top:1785px;font-family:"Questrial",sans-serif;font-weight:700;font-size:35px;color:var(--sky-dark);-webkit-text-stroke:.6px var(--sky-dark)}
.org-name{font-family:"Arimo",sans-serif;font-weight:700;font-size:21px;color:#2c2c2c;display:flex;align-items:center;gap:8px}
.org-name i{display:inline-block;width:18px;height:18px;border-radius:50%;background:var(--link)}
.org-text{width:240px;font-size:13.5px;line-height:19px;color:var(--link)}
.org-text b{font-weight:700}

.footer-bar{top:2307px;height:39px;background:var(--bar)}
.footer-text{left:300px;top:2318px;width:595px;text-align:right;color:var(--white);font-size:14px}
.social{top:2309px;width:34px;height:34px;background:var(--social);border-radius:3px}
</style>
</head>
<body>
<div class="page">

  <nav class="abs topnav">
    <a style="left:551px">Home</a>
    <a style="left:656px">Solution</a>
    <a style="left:795px">About us</a>
    <a style="left:935px">Contact us</a>
    <a style="left:1075px">News</a>
  </nav>

  <div class="abs brand">Marrowvane</div>
  <div class="abs contact" style="left:722px">
    <svg width="22" height="30" viewBox="0 0 22 30"><path d="M5 2c2 0 3 5 3 6s-3 2-3 3c0 4 3 9 6 11 1 0 2-3 3-3s5 2 5 4-2 5-5 5C7 28 1 18 1 9 1 5 3 2 5 2z" fill="var(--sky)"/></svg>
    xxxxx-xxxxxxx
  </div>
  <div class="abs contact" style="left:900px">
    <svg width="46" height="30" viewBox="0 0 46 30"><rect x="2" y="2" width="42" height="26" rx="3" fill="none" stroke="var(--sky)" stroke-width="2.5"/><path d="M3 3l20 15L43 3" fill="none" stroke="var(--sky)" stroke-width="2.5"/></svg>
    sales@xxxxxx.com
  </div>

  <div class="abs banner">
    <div class="slide" role="img" aria-label="Blue line illustration of a server, presenter and support team" style="left:22px;top:31px;width:288px;height:193px;background:linear-gradient(90deg,#cfe4f8,#eaf3fc)"></div>
    <div class="slide" role="img" aria-label="Blue world map banner inviting to join the cloud federation" style="left:333px;top:42px;width:307px;height:173px;background:linear-gradient(135deg,#1c8cc8,#0f6fa8)"></div>
    <div class="slide" role="img" aria-label="Photograph of a server room with a glowing cloud" style="left:678px;top:42px;width:313px;height:173px;background:linear-gradient(180deg,#c9dde6,#3c5f68 60%,#1d3238)"></div>
  </div>

  <div class="abs ask" style="left:106px;top:510px">We don't want to develop Cloud software by ourselves ?</div>
  <div class="abs ask" style="left:106px;top:721px">We don't want to buy new devices.</div>
  <div class="abs ask" style="left:817px;top:510px">We don't want to develop Cloud software by ourselves ?</div>
  <div class="abs ask" style="left:817px;top:721px">We don't want to buy new devices.</div>

  <div class="abs portrait" role="img" aria-label="Photograph of a stressed businessman holding his head, covered with sticky notes"></div>
  <span class="abs qmark red" style="left:414px;top:536px;font-size:20px">?</span>
  <span class="abs qmark red" style="left:512px;top:553px;font-size:58px">?</span>
  <span class="abs qmark red" style="left:659px;top:554px;font-size:42px">?</span>
  <span class="abs qmark blue" style="left:720px;top:528px;font-size:180px">?</span>
  <span class="abs qmark red" style="left:820px;top:615px;font-size:58px">?</span>
  <span class="abs qmark blue" style="left:422px;top:643px;font-size:110px">?</span>
  <span class="abs qmark red" style="left:800px;top:741px;font-size:22px">?</span>

  <div class="abs cta">Please choose Marrowvane !</div>

  <h2 class="abs intro-title">We can start from scatch and provide a fully cloud enviroment.</h2>
  <p class="abs intro-text">We're not a hosting company, so you're not tounching your new cloud services&nbsp; through a compititor. We help you build and manage intrasture to sell cloud business utilising a full application eco-system, All made aforable with single monthly invoices</p>

  <div class="abs service-head" style="left:99px">Consulting</div>
  <div class="abs service-tip" style="left:220px"></div>
  <div class="abs service-body" style="left:99px">Lorem Ipsum is simply dummy text of the printing and type setting industry. Lorem Ipsum has been the industry's standard dummy text ever since the 1500 when an unknown printer took a galley. Lorem Ipsum is simply dummy text of the printing and typesetting industry. Lorem Ipsum has been the industry's standard dummy text ever since the 1500s, when an unknown printer took a galley of type.</div>

  <div class="abs service-head" style="left:460px">Deploying</div>
  <div class="abs service-tip" style="left:581px"></div>
  <div class="abs service-body" style="left:460px">Lorem Ipsum is simply dummy text of the printing and type setting industry. Lorem Ipsum has been the industry's standard dummy text ever since the 1500 when an unknown printer took a galley. Lorem Ipsum is simply dummy text of the printing and typesetting industry. Lorem Ipsum has been the industry's standard dummy text ever since the 1500s, when an unknown printer took a galley of type.</div>

  <div class="abs service-head" style="left:815px">Integration</div>
  <div class="abs service-tip" style="left:936px"></div>
  <div class="abs service-body" style="left:815px">Lorem Ipsum is simply dummy text of the printing and type setting industry. Lorem Ipsum has been the industry's standard dummy text ever since the 1500 when an unknown printer took a galley. Lorem Ipsum is simply dummy text of the printing and typesetting industry. Lorem Ipsum has been the industry's standard dummy text ever since the 1500s, when an unknown printer took a galley of type.</div>

  <h3 class="abs section-title" style="left:99px">Our Customers</h3>
  <h3 class="abs section-title" style="left:675px">Our Partners</h3>

  <div class="abs org-name" style="left:99px;top:1923px"><i></i>Aster Cloud</div>
  <p class="abs org-text" style="left:279px;top:1896px"><b>Aster Cloud</b> is a China-based one-stop cloud solution provider,with more than 10 years experience of cloud deployment,management and operation.</p>

  <div class="abs org-name" style="left:99px;top:2040px"><i></i>Vellum Cloud</div>
  <p class="abs org-text" style="left:279px;top:2032px"><b>Vellum Cloud</b> is a China-based one-stop cloud solution provider,with more than 10 years experience of cloud deployment,management and operation.</p>

  <div class="abs org-name" style="left:99px;top:2190px"><i></i>Qiro Networks</div>
  <p class="abs org-text" style="left:279px;top:2168px"><b>Qiro Networks</b> is a China-based one-stop cloud solution provider,with more than 10 years experience of cloud deployment,management and operation.</p>

  <div class="abs org-name" style="left:678px;top:1911px"><i></i>Stackwell</div>
  <p class="abs org-text" style="left:860px;top:1896px"><b>Aster Cloud</b> is a China-based one-stop cloud solution provider,with more than 10 years experience of cloud deployment,management and operation.</p>

  <div class="abs org-name" style="left:710px;top:2060px"><i></i>Norvex</div>
  <p class="abs org-text" style="left:860px;top:2032px"><b>Vellum Cloud</b> is a China-based one-stop cloud solution provider,with more than 10 years experience of cloud deployment,management and operation.</p>

  <div class="abs footer-bar" style="left:0;width:930px"></div>
  <div class="abs footer-bar" style="left:1118px;width:82px"></div>
  <div class="abs footer-text">© 2014 marrowvane limited | Tel :xxxxxxxxx | supportmarrowvane.com</div>
  <div class="abs social" style="left:950px"></div>
  <div class="abs social" style="left:1003px"></div>
  <div class="abs social" style="left:1055px"></div>

</div>
</body>
</html>
```